M Zyvantics Buisness Cards

I need a technology focused clean business card for my employees. I have attached out logo to include in the mocks. We're a modern tech consulting firm that drives to interface humanity with technology in a truly cohesive fashion.

```html
<!DOCTYPE html>
<html lang="en">
<head>
<meta charset="utf-8">
<title>M Zyvantics Business Cards</title>
<link href="https://fonts.googleapis.com/css2?family=Fira+Sans:wght@500&family=Roboto:wght@400;500&display=swap" rel="stylesheet">
<style>
  :root {
    --backdrop: #a7a7a7;
    --brand-blue: #1b6fb8;
    --brand-blue-deep: #1766ad;
    --card-white: #f4f4f4;
    --brand-grey: #78787b;
    --ink: #3a3a3c;
  }
  * { margin: 0; padding: 0; box-sizing: border-box; }
  html, body { width: 1200px; height: 1138px; overflow: hidden; }
  body {
    background: var(--backdrop);
    font-family: "Roboto", Arial, sans-serif;
    position: relative;
  }
  .card {
    position: absolute;
    border-radius: 14px;
    overflow: hidden;
  }
  .card--front {
    left: 274px; top: 186px; width: 622px; height: 374px;
    background: linear-gradient(180deg, var(--brand-blue) 0%, var(--brand-blue-deep) 100%);
  }
  .card--back {
    left: 276px; top: 608px; width: 618px; height: 373px;
    background: linear-gradient(160deg, #f7f7f7 0%, #ececec 100%);
  }
  .wordmark {
    position: absolute;
    display: flex;
    align-items: center;
    gap: 14px;
    font-family: "Roboto", Arial, sans-serif;
    font-weight: 500;
    white-space: nowrap;
  }
  .wordmark__dot { border-radius: 50%; flex: none; }
  .card--front .wordmark {
    left: 0; right: 0; top: 150px; justify-content: center;
    color: #ffffff; font-size: 60px;
  }
  .card--front .wordmark__dot { width: 22px; height: 22px; background: #ffffff; }
  .card--back .wordmark {
    right: 28px; top: 58px;
    color: var(--brand-grey); font-size: 48px;
  }
  .card--back .wordmark__dot { width: 18px; height: 18px; background: var(--brand-grey); }
  .person { position: absolute; left: 28px; top: 198px; }
  .person__name {
    font-family: "Fira Sans", Arial, sans-serif;
    font-weight: 500; font-size: 21px; color: var(--brand-blue);
  }
  .person__role { font-size: 14px; color: var(--ink); margin-top: 4px; }
  .divider {
    position: absolute; left: 24px; width: 570px; top: 261px;
    height: 2px; background: var(--brand-blue);
  }
  .contacts {
    position: absolute; left: 28px; top: 282px;
    list-style: none; font-size: 16px; color: var(--ink);
  }
  .contacts li { display: flex; align-items: center; gap: 10px; height: 21px; }
  .contacts svg { width: 13px; height: 13px; fill: var(--brand-blue); flex: none; }
  .address {
    position: absolute; right: 52px; top: 301px;
    text-align: right; font-size: 16px; line-height: 21px; color: var(--ink);
    font-style: normal;
  }
</style>
</head>
<body>
  <section class="card card--front">
    <div class="wordmark"><span class="wordmark__dot"></span>M Zyvantics</div>
  </section>

  <section class="card card--back">
    <div class="wordmark"><span class="wordmark__dot"></span>M Zyvantics</div>
    <div class="person">
      <div class="person__name">John Doe Smith</div>
      <div class="person__role">Managing Director</div>
    </div>
    <div class="divider"></div>
    <ul class="contacts">
      <li><svg viewBox="0 0 16 16"><path d="M3 5c0-2 2-3 5-3s5 1 5 3v1h-3V5H6v1H3zM4 8h8l2 6H2z"/></svg>555.555.5555</li>
      <li><svg viewBox="0 0 16 16"><path d="M1 3h14v10H1zM2 4l6 5 6-5v1.5L8 10.5 2 5.5z" fill-rule="evenodd"/></svg>johndoe@example.com</li>
      <li><svg viewBox="0 0 16 16"><path d="M8 1a7 7 0 1 0 0 14A7 7 0 0 0 8 1zm0 1.5c.8 0 1.8 1.6 2.1 4H5.9C6.2 4.1 7.2 2.5 8 2.5zM2.6 7.5h2.3c0 .4 0 .7.1 1H2.6zm8.4 0h2.4v1H11zM5.9 9.5h4.2c-.3 2.4-1.3 4-2.1 4s-1.8-1.6-2.1-4z"/></svg>www.yourwebsite.com</li>
    </ul>
    <address class="address">234 Anywhere St., Any City,<br>Any Town, US 123456</address>
  </section>
</body>
</html>
```